PWT other templates

1) Internal pages for the documents that we write. basically what will the pages inside look like. It should basically be a document with a header, a footer and a page number locator. It should include the following information: name of the report, date, PWT logo somehow, and version (draft, final etc). the information should be divided between header and footer. let me know if its unclear. As with everything it should work both in black and white and in color in case it is printed in black and white :-)
2) chapter dividers. This are the pages that you might have inside the report to separate sections. It should just have a page number, and chapter or section name. Simple, but again follow the same idea of the design that you created. It should be possible to have a picture in the divider, but it should not be a must. so in that sense we need to versions.
3) Business cards. Should include space for name, title, phone numbers (2 or 3), email, Skype, web page, and the company address which you have already.
4) a signature for emails. Basically the file that is glued to the bottom off all emails as a signature. Again it should include all the information in the business cards.

Not including any files since you have already designed others

```html
<!DOCTYPE html>
<html lang="en">
<head>
<meta charset="utf-8">
<title>Subject of the page</title>
<link rel="stylesheet" href="https://fonts.googleapis.com/css2?family=Arimo:wght@700&family=EB+Garamond:wght@400&family=Source+Sans+3:wght@400;600&display=swap">
<style>
  :root {
    --green-deep: #6fae2f;
    --green-mid: #8cc43f;
    --green-light: #a8d14a;
    --green-pale: #c6e27c;
    --paper: #ffffff;
    --ink-body: #505050;
    --ink-logo: #111111;
  }
  html, body {
    margin: 0;
    padding: 0;
    overflow: hidden;
    background: var(--paper);
  }
  .page {
    position: relative;
    width: 1200px;
    height: 848px;
    overflow: hidden;
    background: var(--paper);
  }
  .page-art {
    position: absolute;
    inset: 0;
    width: 1200px;
    height: 848px;
  }
  .page-title {
    position: absolute;
    left: 44px;
    top: 88px;
    margin: 0;
    font-family: "Arimo", Arial, sans-serif;
    font-weight: 700;
    font-size: 49px;
    line-height: 1;
    color: var(--paper);
  }
  .report-meta {
    position: absolute;
    right: 44px;
    top: 26px;
    margin: 0;
    display: flex;
    gap: 22px;
    font-family: "Source Sans 3", "Myriad Pro", sans-serif;
    font-size: 17px;
    line-height: 1;
    color: var(--paper);
  }
  .report-meta__label {
    font-weight: 600;
  }
  .body-column {
    position: absolute;
    margin: 0;
    font-family: "Source Sans 3", "Myriad Pro", sans-serif;
    font-size: 26.4px;
    line-height: 32.8px;
    color: var(--ink-body);
    white-space: nowrap;
  }
  .body-column p { margin: 0 0 4px; }
  .body-column--left { left: 139px; top: 234px; }
  .body-column--right { left: 650px; top: 238px; }
  .footer-logo {
    position: absolute;
    left: 60px;
    top: 770px;
    margin: 0;
    font-family: "EB Garamond", Garamond, serif;
    font-size: 48px;
    line-height: 1;
    color: var(--ink-logo);
  }
  .page-number {
    position: absolute;
    left: 1024px;
    top: 797px;
    margin: 0;
    font-family: "EB Garamond", Garamond, serif;
    font-size: 21px;
    line-height: 1;
    color: var(--paper);
  }
</style>
</head>
<body>
<div class="page">
  <svg class="page-art" viewBox="0 0 842 595" preserveAspectRatio="none">
    <defs>
      <linearGradient id="header-fill" x1="0" y1="0" x2="1" y2="0.3">
        <stop offset="0" stop-color="var(--green-light)"/>
        <stop offset="0.5" stop-color="var(--green-mid)"/>
        <stop offset="1" stop-color="var(--green-deep)"/>
      </linearGradient>
      <linearGradient id="footer-fill" x1="0" y1="0" x2="1" y2="0">
        <stop offset="0" stop-color="var(--green-pale)"/>
        <stop offset="0.45" stop-color="var(--green-light)"/>
        <stop offset="1" stop-color="var(--green-mid)"/>
      </linearGradient>
    </defs>
    <g class="header-band" role="img" aria-label="Green header band with a faceted geometric texture">
      <path class="header-band__edge" fill="var(--green-pale)"
            d="M0,0 H842 V126 C800,96 740,82 660,85 C520,90 400,126 250,129 C150,131 60,126 0,121 Z"/>
      <path class="header-band__main" fill="url(#header-fill)"
            d="M0,0 H842 V120 C800,90 740,75 660,78 C520,83 400,118 250,121 C150,123 60,118 0,113 Z"/>
    </g>
    <path class="footer-band" role="img" aria-label="Green footer wave with a faceted geometric texture"
          fill="url(#footer-fill)"
          d="M30,513 C180,504 330,503 430,518 C540,535 600,562 680,561 C760,560 815,520 842,480 V595 H470 C400,560 250,522 30,513 Z"/>
  </svg>

  <h1 class="page-title">Subject of the page</h1>

  <p class="report-meta">
    <span class="report-meta__item"><span class="report-meta__label">Report:</span> Report name</span>
    <span class="report-meta__item"><span class="report-meta__label">Date:</span> 00.00.0000</span>
    <span class="report-meta__item"><span class="report-meta__label">Version:</span> Draft</span>
  </p>

  <div class="body-column body-column--left">
    <p>Lorem ipsum dolor sit amet, consectet<br>adipiscing elit, sed diam nonummy nib<br>euismod tincidunt ut laoreet dolore ma<br>aliquam erat volutpat. Ut wisi enim ad</p>
    <p>Lorem ipsum dolor sit amet, consectet<br>adipiscing elit, sed diam nonummy nib<br>euismod tincidunt ut laoreet dolore ma<br>aliquam erat volutpat. Ut wisi enim ad</p>
    <p>Lorem ipsum dolor sit amet, consectet<br>adipiscing elit, sed diam nonummy nib<br>euismod tincidunt ut laoreet dolore ma<br>aliquam erat volutpat. Ut wisi enim ad</p>
  </div>

  <div class="body-column body-column--right">
    <p>minim veniam, quis nostrud exerci tatio<br>ullamcorper suscipit lobortis nisl ut aliqu<br>ex ea commodo consequat. Duis autem<br>eum iriure dolor in hendrerit in vulputat</p>
    <p>minim veniam, quis nostrud exerci tatio<br>ullamcorper suscipit lobortis nisl ut aliqu<br>ex ea commodo consequat. Duis autem<br>eum iriure dolor in hendrerit in vulputat</p>
    <p>minim veniam, quis nostrud exerci tatio<br>ullamcorper suscipit lobortis nisl ut aliqu<br>ex ea commodo consequat. Duis autem<br>eum iriure dolor in hendrerit in vulputat</p>
  </div>

  <p class="footer-logo">LOGO</p>
  <p class="page-number">Page NO#</p>
</div>
</body>
</html>
```